Web Design Project - Shipping Industry

Goals and Objectives
The objective of the new website is to create a more modern look and feel. The site will also allow for a more effective means of communicating with members while providing the public with information and developments in the local, regional and international shipping industry.
Scope
The website will highlight the history of the organisation inclusive of text and photographs. It will take visitors through the years from beginning to present. Information on the history of the shipping industry will also be included.
It will feature current articles on the organisation, its members and stakeholders in the shipping industry. Member information as well as pertinent details regarding the organisation’s subsidiaries will be documented for the website.
Information as it relates to shipping statistics, case studies, laws and regulations, international treaties and trade documents, shipping terms, careers in shipping, job opportunities, training opportunities, information for shippers including port listing and trade lanes will be main features of the content for the website.
The Association’s community involvement, industry calendar events and related links relevant industry members will also be featured.
Target Market
• The General Public;
• Members of the organization;
• Shipping Industry Stakeholders (local, regional and international);
• Tertiary students conducting research.
• Potential employees
• Potential Business Partners
Best Practice Bench Marketing
The following websites are being looked at:
• Korvel Quays - http://www.korvelquays.example/ (preferred look)
• Tidewell Shipping Association - http://www.twa-ships.example/ (like image transition on main page)
• Brolund - http://www.brolund.example (professional look)
• KHW - http://www.kelharbours.example (preferred color: blue in logo)
• Vendlo - http://www.vendlo.example/electronics/tv-video-audio/ (preferred look for links page: image + short text below + visit site link)
Expected Result
• 3 - 5 pages which must include: [1] main page [2] standard page [3] links page
Target Market(s)
The General Public; Members of the organization; Shipping Industry Stakeholders (local, regional and international); Tertiary students conductin
Industry/Entity Type
Shipping

```html
<!DOCTYPE html>
<html lang="en">
<head>
<meta charset="utf-8">
<title>The Shipping Association Of Kelmara</title>
<link href="https://fonts.googleapis.com/css2?family=Questrial&family=Sorts+Mill+Goudy&family=Noto+Sans:wght@400;600&display=swap" rel="stylesheet">
<style>
:root{
  --navy:#0b3aa6;
  --navy-dark:#062a80;
  --link:#1a3c9a;
  --orange:#f2a300;
  --text:#333;
  --muted:#777;
  --rule:#d4d4d4;
  --footer:#cacaca;
  --heading:#1f2a66;
}
*{margin:0;padding:0;box-sizing:border-box}
html,body{width:1008px;height:1200px;overflow:hidden;background:#fff}
body{position:relative;font-family:"Noto Sans",Verdana,sans-serif;color:var(--text);font-size:9.5px}
.abs{position:absolute}
/* header */
.brand-mark{left:100px;top:24px;width:66px;height:66px;border-radius:50%;background:var(--navy)}
.brand-name{left:100px;top:96px;font-family:"Sorts Mill Goudy",Georgia,serif;font-size:20px;color:var(--navy);white-space:nowrap}
.login-label{left:403px;top:22px;font-size:10.5px;letter-spacing:.6px;color:var(--navy-dark)}
.field{top:18px;width:160px;height:21px;border:2px solid #d6d6d6;border-radius:11px;font-size:9px;color:#888;padding:3px 12px}
.login-btn{left:848px;top:17px;width:60px;height:22px;background:var(--orange);border-radius:3px;color:#fff;font-weight:600;font-size:10px;text-align:center;line-height:22px;letter-spacing:.3px}
.account-links{top:54px;font-size:9.5px;color:#333}
.account-divider{left:800px;top:51px;width:1px;height:17px;background:#888}
/* nav */
.main-nav{left:100px;top:145px;height:29px;width:807px}
.main-nav a{position:absolute;top:0;height:29px;line-height:29px;font-family:"Questrial",sans-serif;font-size:11px;color:var(--navy);text-decoration:none;white-space:nowrap}
.main-nav a.active{background:var(--navy);color:#fff;padding:0 9px}
/* announcement */
.announce{left:100px;top:192px;width:807px;height:54px;background:var(--navy)}
.announce-box{left:4px;top:4px;width:601px;height:45px;background:#fff;border:1px solid var(--navy)}
.announce-label{left:22px;top:16px;font-family:"Questrial",sans-serif;font-size:11px;color:var(--orange)}
.announce-text{left:150px;top:16px;font-size:9.5px;color:#333;white-space:nowrap}
.search-label{left:675px;top:10px;font-family:"Questrial",sans-serif;font-size:10.5px;color:var(--orange)}
.search-field{left:637px;top:28px;width:147px;height:14px;background:#fff;border-radius:7px}
.search-btn{left:760px;top:28px;width:24px;height:14px;background:var(--orange);border-radius:7px}
/* hero */
.hero{left:100px;top:255px;width:807px;height:381px;border:3px solid #a8c8ee;background:linear-gradient(180deg,#9fcde6 0%,#c8e2ee 42%,#4f77a6 52%,#3d5f8c 80%,#2c4d7c 100%)}
.hero-band{left:0;bottom:0;width:801px;height:47px;background:rgba(30,35,45,.78)}
.dot{top:601px;width:6px;height:6px;border-radius:50%;background:#fff}
/* content */
.card{top:664px;width:267px;height:205px}
.card.framed{border:1px solid #f2c766;outline:1px solid #f2c766;outline-offset:-4px}
.card h2{position:absolute;left:14px;top:14px;font-family:"Questrial",sans-serif;font-size:13px;font-weight:400;color:var(--heading);letter-spacing:.3px;-webkit-text-stroke:.3px var(--heading);white-space:nowrap}
.card .rule{position:absolute;left:14px;right:12px;top:36px;height:1px;background:var(--rule)}
.card p{position:absolute;left:14px;width:240px;font-size:9.5px;line-height:11px;color:#333}
.read-more{position:absolute;left:165px;top:168px;width:83px;height:23px;background:var(--navy);color:#fff;font-size:9.5px;text-align:center;line-height:23px;border-radius:2px}
.col-divider{left:678px;top:670px;width:1px;height:212px;background:var(--rule)}
.side-title{left:707px;font-family:"Questrial",sans-serif;font-size:13.5px;color:#333}
.side-list{left:716px;list-style:none}
.side-list li{position:relative;height:15px;padding-left:13px;font-size:9.5px;color:var(--link);letter-spacing:.3px;white-space:nowrap}
.side-list li::before{content:"";position:absolute;left:0;top:4px;width:6px;height:6px;border:1.5px solid var(--orange);border-radius:50%}
.section-rule{left:100px;top:912px;width:807px;height:1px;background:var(--rule)}
/* partners */
.partner{top:952px;font-size:14px;font-weight:600;color:var(--navy-dark);white-space:nowrap}
/* footer */
.footer{left:100px;top:1027px;width:807px;height:173px;background:var(--footer)}
.footer-nav{top:24px;font-size:9.5px;color:var(--link);white-space:nowrap}
.footer-mark{left:28px;top:61px;width:44px;height:44px;border-radius:50%;background:var(--navy)}
.footer-name{left:28px;top:111px;font-family:"Sorts Mill Goudy",Georgia,serif;font-size:14px;color:var(--navy);white-space:nowrap}
.copyright{left:28px;top:139px;font-size:9px;color:#666}
.connect-title{left:590px;top:21px;font-family:"Questrial",sans-serif;font-size:13.5px;color:#333}
.connect-box{left:590px;top:42px;width:193px;height:85px;background:#fff;border:1px solid #ddd;padding:12px 12px 0}
.connect-box p{font-size:8.5px;line-height:10px;color:#333}
.connect-meta{margin-top:6px;font-size:8.5px;color:#d94a10}
.connect-meta em{margin-left:8px}
.social{top:135px;width:24px;height:24px;border-radius:50%;background:var(--navy);border:2px solid #e8eef8}
</style>
</head>
<body>

<header>
  <div class="abs brand-mark"></div>
  <div class="abs brand-name">The Shipping Association Of Kelmara</div>

  <div class="abs login-label">MEMBER LOGIN:</div>
  <div class="abs field" style="left:506px">User ID</div>
  <div class="abs field" style="left:675px">Password</div>
  <div class="abs login-btn">LOG IN</div>
  <div class="abs account-links" style="left:738px">Register</div>
  <div class="abs account-divider"></div>
  <div class="abs account-links" style="left:818px">Forgot password?</div>

  <nav class="abs main-nav">
    <a class="active" style="left:0">ABOUT US</a>
    <a style="left:86px">SHIPPING SCHEDULE</a>
    <a style="left:215px">NEWS</a>
    <a style="left:266px">FAQ</a>
    <a style="left:311px">CONTACT US</a>
    <a style="left:407px">CANINE SERVICES</a>
    <a style="left:527px">PORTLYN</a>
    <a style="left:614px">LINKS</a>
  </nav>
</header>

<section class="abs announce">
  <div class="abs announce-box">
    <div class="abs announce-label">ANNOUNCEMENTS:</div>
    <div class="abs announce-text">Welcome to the KHW's website: We work the Port of Kelhaven...</div>
  </div>
  <div class="abs search-label">SEARCH SITE</div>
  <div class="abs search-field"></div>
  <div class="abs search-btn"></div>
</section>

<section class="abs hero" role="img" aria-label="Photo of a harbour pier with cargo cranes, containers and a docked ship under a clear sky">
  <div class="abs hero-band"></div>
</section>
<div class="abs dot" style="left:792px;background:#555"></div>
<div class="abs dot" style="left:809px"></div>
<div class="abs dot" style="left:826px"></div>
<div class="abs dot" style="left:842px"></div>
<div class="abs dot" style="left:858px"></div>
<div class="abs dot" style="left:875px"></div>

<main>
  <article class="abs card framed" style="left:100px">
    <h2>About The Association</h2>
    <div class="rule"></div>
    <p style="top:55px">Registered as a Trade Union, one of the primary functions of the Association is to regulate the daily supply and management of certain categories of labour on the Port.</p>
    <p style="top:105px">&nbsp;In addition, the Association acts on behalf of its members in initiatives to advance industrial relations, training, security, information ...</p>
    <div class="read-more">Read More</div>
  </article>

  <article class="abs card" style="left:380px">
    <h2 style="top:10px">Invitation To Tender</h2>
    <div class="rule" style="left:14px;right:0"></div>
    <p style="top:55px;width:250px">The Port Authority of Kelmara now invites sealed bids from eligible and qualified bidders for the design, development, supply and commissioning of a Port Community System for Kelmara utilizing the International Competitive Tender Procurement Methodology.</p>
    <p style="top:128px;width:250px">The design, development, delivery/commissioning period is estimated at two (2) years. .....</p>
    <div class="read-more">Read More</div>
  </article>

  <div class="abs col-divider"></div>

  <aside>
    <div class="abs side-title" style="top:673px">Links</div>
    <ul class="abs side-list" style="top:697px">
      <li>Training Courses</li>
      <li>About the Port of Kelhaven</li>
      <li>Open Tenders</li>
    </ul>
    <div class="abs side-title" style="top:783px">Important Facts</div>
    <ul class="abs side-list" style="top:807px">
      <li>Laws and Legislation</li>
      <li>International trade Docs</li>
      <li>Port Statistics</li>
      <li>Shipping Terms</li>
    </ul>
  </aside>

  <div class="abs section-rule"></div>

  <section aria-label="Member companies">
    <div class="abs partner" style="left:130px">Velmora Line</div>
    <div class="abs partner" style="left:292px">Quellsea</div>
    <div class="abs partner" style="left:404px">Brantor Shipping</div>
    <div class="abs partner" style="left:590px">Halvenik Shipping</div>
    <div class="abs partner" style="left:752px">Orvena Shipping</div>
  </section>
</main>

<footer class="abs footer">
  <div class="abs footer-nav" style="left:28px">Shipping Schedule</div>
  <div class="abs footer-nav" style="left:133px">News</div>
  <div class="abs footer-nav" style="left:177px">Faq</div>
  <div class="abs footer-nav" style="left:215px">Contact Us</div>
  <div class="abs footer-nav" style="left:291px">Canine Services</div>
  <div class="abs footer-nav" style="left:390px">Portlyn</div>
  <div class="abs footer-nav" style="left:460px">Links</div>

  <div class="abs footer-mark"></div>
  <div class="abs footer-name">The Shipping Association Of Kelmara</div>
  <div class="abs copyright">© Copyright 2012. All Rights Reserved.</div>

  <div class="abs connect-title">Connect With Us</div>
  <div class="abs connect-box">
    <p>Praesent tempus sagittis elementum. Prsent id quam erat, sit amet condi mentum neque. Phasellus quis est nisi. Ut luctus adipiscing.</p>
    <div class="connect-meta">Lorem Ipsum <em>2 hours ago</em></div>
  </div>
  <div class="abs social" style="left:592px"></div>
  <div class="abs social" style="left:621px"></div>
  <div class="abs social" style="left:651px"></div>
  <div class="abs social" style="left:683px"></div>
</footer>

</body>
</html>
```